Tidal Brookfield ( New Product Range Office Furniture )

We are looking a dedicated page within our website www.quarnex.com.au ( must be Magento compatible ) to launch our new brand " TIDAL Brookfield "

We have our existing Brand "KEMO" has been selling in the last 10 years in Australia, We have just manufactured our new range please go our website and type "Tidal" in the search box.

The ideal is to have this page to showcase our new products in more professional manner, target audience is corporate customers.

We are also working with a office designers who they will use our website to show their clients with our products

Key Note
This web page is an additional page to be added to our existing website,

so WE DO NOT NEED SHOPPING CART in these pages,

Which means, when customer click on these pages, they will see a total corporate presentation of our Tidal Brookfield.

What we want to see is below

We want to showcase each product individually with main image with Long Description, because our product is a modular system we want to add thumbnail images to show 4 more different type of combination images (images to be provided later) so total of 5 images (we can live with 4 images if better spacing when design)

we need a good background theme to make sure they are all match nicely

Hope the above notes will help you get us a better design

Target Market(s)

Corporate End Users, Also Office Interior Designers

Industry/Entity Type

Office Furniture

Number of Pages Required

2 page

Font styles to use
Sans Serif

Requirements
Must have
• Our Tidal Brookfield product images ( can get from our website for now )
Nice to have
• Our Product Tidal Brookfield Range is a modular system, there are so many configuration that our customer can use to setup their office

```html
<!DOCTYPE html>
<html lang="en">
<head>
<meta charset="utf-8">
<title>Tidal Brookfield – Desking</title>
<link href="https://fonts.googleapis.com/css2?family=Open+Sans:wght@400;600;700&family=Oswald:wght@500&display=swap" rel="stylesheet">
<style>
:root{
  --orange:#f58a45;
  --nav:#414141;
  --ink:#222;
  --text:#444;
  --line:#dedede;
  --footer:#050505;
  --footer-base:#1e1e1e;
  --footer-link:#b5b5b5;
  --badge:#8a1424;
  --thumb:#d9d4cc;
}
*{box-sizing:border-box;margin:0;padding:0}
html,body{width:770px;height:1200px;overflow:hidden;background:#fff}
body{font-family:"Open Sans",Arial,sans-serif;color:var(--text);position:relative}
.topline{height:2px;background:var(--orange)}
.header{height:56px;position:relative}
.logo{position:absolute;left:84px;top:13px;font-family:"Oswald",sans-serif;font-weight:500;font-size:22px;color:var(--orange);letter-spacing:.2px}
.search{position:absolute;left:268px;top:16px;width:238px;height:24px;border:1px solid #ccc;display:flex;font-size:7px}
.search .cat{width:66px;border-right:1px solid #ccc;display:flex;align-items:center;padding-left:6px;gap:4px;color:#555}
.search .field{flex:1;display:flex;align-items:center;padding-left:8px;color:#999;font-style:italic}
.search .go{width:27px;background:#333;display:flex;align-items:center;justify-content:center}
.account{position:absolute;left:513px;top:16px;height:24px;display:flex}
.account a{background:var(--orange);color:#fff;font-size:7px;font-weight:700;display:flex;align-items:center;padding:0 8px;text-decoration:none}
.nav{height:42px;background:var(--nav);position:relative}
.nav-item{position:absolute;top:0;height:42px;display:flex;flex-direction:column;align-items:center;justify-content:center;gap:3px;color:#fff;font-size:7.2px;font-weight:700;transform:translateX(-50%);white-space:nowrap}
.nav-item.active{background:var(--orange);width:55px}
.nav-item svg{width:16px;height:14px}
.catalog{position:absolute;left:83px;top:125px;width:603px;height:835px;border:1px solid var(--line);display:flex}
.sidebar{width:146px;flex:none;border-right:1px solid var(--line)}
.filter{border-bottom:1px solid var(--line);padding:13px 10px 12px 14px}
.filter:last-child{border-bottom:none}
.filter h3{color:var(--orange);font-size:8px;font-weight:700;margin-bottom:9px}
.filter li{list-style:none;display:flex;justify-content:space-between;font-size:7.3px;color:#333;line-height:1.3;margin-bottom:4px;padding-left:1px}
.filter li.on{color:var(--orange)}
.filter.types li{margin-bottom:10px}
.filter.types li span:first-child{width:110px}
.more{font-size:6.5px;font-weight:700;color:var(--orange);margin:8px 0 0 4px;display:block}
.swatch{display:flex;align-items:center;gap:7px;font-size:7.3px}
.swatch i{width:10px;height:10px;background:#a39179;display:block}
.content{flex:1;min-width:0;padding:0 8px}
.content-head{height:37px;border-bottom:1px solid var(--line);display:flex;align-items:center;justify-content:space-between;padding:0 2px}
.content-head h1{color:var(--orange);font-size:12px;font-weight:600}
.sort{display:flex;align-items:center;gap:8px;font-size:6.5px;color:#444}
.sort .box{width:65px;height:18px;border:1px solid #ccc;display:flex;align-items:center;justify-content:space-between;padding:0 6px;color:#999}
.grid{display:grid;grid-template-columns:repeat(3,1fr);grid-template-rows:190px 196px 204px 200px;margin-top:8px;column-gap:2px}
.card{padding:6px 8px;position:relative;min-width:0}
.card.hover{border:1px solid #ddd;box-shadow:0 0 3px rgba(0,0,0,.12)}
.photo{height:104px;background:linear-gradient(180deg,#fff 0%,#f3f3f3 30%,#b4a58f 42%,#2f2f2f 55%,#222 80%,#fff 100%);border-radius:2px}
.badge{position:absolute;top:16px;right:16px;width:22px;height:22px;border-radius:50%;background:var(--badge);border:2px solid #fff;box-shadow:0 0 0 1px var(--badge);color:#fff;font-size:3.6px;font-weight:700;display:flex;align-items:center;justify-content:center;text-align:center;line-height:1.1}
.quick{position:absolute;left:46px;top:62px;background:var(--orange);color:#fff;font-size:7.5px;font-weight:700;padding:6px 9px}
.card h2{font-size:7.3px;font-weight:600;color:var(--ink);margin-top:10px;line-height:1.4;text-transform:uppercase}
.thumbs{display:flex;gap:4px;margin-top:6px}
.thumbs span{width:24px;height:16px;background:linear-gradient(180deg,#f1efeb 0%,var(--thumb) 45%,#3a3a3a 100%);border:1px solid #e4e4e4;display:block}
.footer{position:absolute;left:0;top:994px;width:770px;height:172px;background:var(--footer);color:var(--footer-link)}
.footer .flogo{position:absolute;left:84px;top:25px;font-family:"Oswald",sans-serif;font-weight:500;font-size:22px;color:var(--orange)}
.follow{position:absolute;left:146px;top:88px;font-size:7.5px;font-weight:700;color:#fff}
.socials{position:absolute;left:111px;top:106px;display:flex;gap:7px}
.socials span{width:20px;height:20px;border-radius:50%;background:#555;display:block}
.fcol{position:absolute;top:26px;font-size:7px;line-height:13px;color:var(--footer-link)}
.fcol h4{color:#fff;font-size:7.5px;font-weight:700;margin-bottom:7px}
.news{position:absolute;left:540px;top:50px;width:148px;height:28px;background:#333;display:flex;align-items:center;padding-left:10px;gap:10px;font-size:7px;color:#bbb}
.signup{position:absolute;left:540px;top:88px;width:148px;height:28px;background:var(--orange);color:#fff;font-family:"Oswald",sans-serif;font-size:11px;display:flex;align-items:center;justify-content:center}
.base{position:absolute;left:0;top:1166px;width:770px;height:34px;background:var(--footer-base);color:#bbb;font-size:6.5px;display:flex;align-items:center;justify-content:center}
</style>
</head>
<body>
<div class="topline"></div>
<header class="header">
  <div class="logo">TIDAL BROOKFIELD</div>
  <div class="search">
    <div class="cat"><svg width="6" height="4"><path d="M0 0h6L3 4z" fill="#555"/></svg>All Categories</div>
    <div class="field">Search Products</div>
    <div class="go"><svg width="11" height="11" viewBox="0 0 11 11"><circle cx="4.5" cy="4.5" r="3.3" stroke="#fff" stroke-width="1.5" fill="none"/><path d="M7 7l3 3" stroke="#fff" stroke-width="1.6"/></svg></div>
  </div>
  <div class="account"><a>MY ACCOUNT</a></div>
</header>
<nav class="nav">
  <div class="nav-item active" style="left:102px"><svg viewBox="0 0 16 14"><path d="M1 4h14M2 4v8M14 4v8M9 4v8M9 7h5M9 10h5" stroke="#fff" fill="none"/></svg>DESKING</div>
  <div class="nav-item" style="left:171px"><svg viewBox="0 0 16 14"><path d="M3 2h10v5H3zM2 7h12M3 7v6M13 7v6" stroke="#fff" fill="none"/></svg>SEATING</div>
  <div class="nav-item" style="left:247px"><svg viewBox="0 0 16 14"><path d="M3 1h10v12H3zM3 5h10M3 9h10M7 3h2M7 7h2M7 11h2" stroke="#fff" fill="none"/></svg>STORAGE</div>
  <div class="nav-item" style="left:324px"><svg viewBox="0 0 16 14"><rect x="3" y="3" width="10" height="10" fill="#fff"/><path d="M4 1h8" stroke="#fff"/></svg>SCREENS</div>
  <div class="nav-item" style="left:400px"><svg viewBox="0 0 16 14"><path d="M1 3h14M8 3v10M5 13h6" stroke="#fff" stroke-width="1.3" fill="none"/></svg>TABLES</div>
  <div class="nav-item" style="left:492px"><svg viewBox="0 0 16 14"><path d="M1 7h14v6H1zM3 7V4h4v3M9 2h4v5" stroke="#fff" fill="none"/></svg>RECEPTION COUNTERS</div>
  <div class="nav-item" style="left:589px"><svg viewBox="0 0 16 14"><path d="M8 13C4 8 4 6 4 5a4 4 0 0 1 8 0c0 1 0 3-4 8z" fill="#fff"/><circle cx="8" cy="5" r="1.5" fill="#414141"/></svg>WHERE TO BUY</div>
  <div class="nav-item" style="left:669px"><svg viewBox="0 0 16 14"><path d="M1 2h14v10H1zM1 2l7 6 7-6" stroke="#fff" fill="none"/></svg>CONTACT</div>
</nav>

<main class="catalog">
  <aside class="sidebar">
    <section class="filter">
      <h3>CATEGORY</h3>
      <ul><li class="on"><span>Desking</span><span>(14)</span></li><li><span>Storage</span><span>(10)</span></li><li><span>Tables</span><span>(9)</span></li></ul>
    </section>
    <section class="filter">
      <h3>SIZE</h3>
      <ul>
        <li><span>1200(L) x 380(D) x 1070(H)</span><span>(1)</span></li>
        <li><span>1800(L) x 380(D) x 1070(H)</span><span>(1)</span></li>
        <li><span>1800(L) x 600(D) x 725(H)</span><span>(1)</span></li>
        <li><span>1800(L) x 380(D) x 1070(H)</span><span>(1)</span></li>
        <li><span>1800(L) x 600(D) x 725(H)</span><span>(1)</span></li>
        <li><span>1800(L) x 600(D) x 900(H)</span><span>(1)</span></li>
        <li><span>1800(L) x 800(D) x 725(H)</span><span>(1)</span></li>
        <li><span>1800(L) x 950/830(D) x 725(H)</span><span>(1)</span></li>
        <li><span>1800(L) x 315(D) x 1050(H)</span><span>(1)</span></li>
        <li><span>1500(L) x 800(D) x 725(H)</span><span>(1)</span></li>
      </ul>
      <span class="more">MORE &#9656;</span>
    </section>
    <section class="filter">
      <h3>COLOUR</h3>
      <div class="swatch"><i></i>(34)</div>
    </section>
    <section class="filter types">
      <h3>PRODUCT TYPE</h3>
      <ul>
        <li><span>NEW-FU-DKS &amp; CWS</span><span>(1)</span></li>
        <li><span>NEW-FURNITURE-PEDESTAL DRAWERS-MOBILE PEDESTALS</span><span>(1)</span></li>
        <li><span>NEW-FURNITURE-STORAGE CABINETS-CREDENZAS</span><span>(1)</span></li>
        <li><span>NEW-FURNITURE-STORAGE CABINETS-DOORED CABINETS</span><span>(1)</span></li>
        <li><span>NEW-FURNITURE-STORAGE CABINETS-SIDEBOARDS</span><span>(1)</span></li>
        <li><span>NEW-FURNITURE-TABLES-CONFERENCE TABLES</span><span>(1)</span></li>
      </ul>
      <span class="more">MORE &#9656;</span>
    </section>
  </aside>

  <section class="content">
    <div class="content-head">
      <h1>Desking</h1>
      <div class="sort">Sort by <span class="box">Popularity <svg width="7" height="4"><path d="M0 0l3.5 3.5L7 0" stroke="#999" fill="none"/></svg></span></div>
    </div>
    <div class="grid">
      <article class="card hover"><div class="photo" role="img" aria-label="Tidal Brookfield 1580 desk product photo"></div><span class="badge">NEW COLOUR</span><span class="quick">QUICK VIEW</span><h2>Tidal Brookfield 1580 Desk</h2><div class="thumbs" role="img" aria-label="Four configuration views"><span></span><span></span><span></span><span></span></div></article>
      <article class="card"><div class="photo" role="img" aria-label="Tidal Brookfield 1200 desk product photo"></div><span class="badge">NEW COLOUR</span><h2>Tidal Brookfield 1200 Desk Return</h2><div class="thumbs" role="img" aria-label="Four configuration views"><span></span><span></span><span></span><span></span></div></article>
      <article class="card"><div class="photo" role="img" aria-label="Tidal Brookfield 1500 corner desk product photo"></div><span class="badge">NEW COLOUR</span><h2>Tidal Brookfield 1500 Corner Desk (Left Return)</h2><div class="thumbs" role="img" aria-label="Four configuration views"><span></span><span></span><span></span><span></span></div></article>
      <article class="card"><div class="photo" role="img" aria-label="Tidal Brookfield 2100 P-end desk right product photo"></div><span class="badge">NEW COLOUR</span><h2>Tidal Brookfield 2100 P-End Desk - Right</h2><div class="thumbs" role="img" aria-label="Four configuration views"><span></span><span></span><span></span><span></span></div></article>
      <article class="card"><div class="photo" role="img" aria-label="Tidal Brookfield desk return product photo"></div><span class="badge">NEW COLOUR</span><h2>Tidal Brookfield Desk Return 1000 x 600</h2><div class="thumbs" role="img" aria-label="Four configuration views"><span></span><span></span><span></span><span></span></div></article>
      <article class="card"><div class="photo" role="img" aria-label="Tidal Brookfield 2100 P-end desk left product photo"></div><span class="badge">NEW COLOUR</span><h2>Tidal Brookfield 2100 P-End Desk - Left</h2><div class="thumbs" role="img" aria-label="Four configuration views"><span></span><span></span><span></span><span></span></div></article>
      <article class="card"><div class="photo" role="img" aria-label="Tidal Brookfield 2100 P-end desk left product photo"></div><span class="badge">NEW COLOUR</span><h2>Tidal Brookfield 2100 P-End Desk - Left</h2><div class="thumbs" role="img" aria-label="Four configuration views"><span></span><span></span><span></span><span></span></div></article>
      <article class="card"><div class="photo" role="img" aria-label="Tidal Brookfield corner desk return left product photo"></div><span class="badge">NEW COLOUR</span><h2>Tidal Brookfield 1800/900 Corner Desk Return - Left</h2><div class="thumbs" role="img" aria-label="Four configuration views"><span></span><span></span><span></span><span></span></div></article>
      <article class="card"><div class="photo" role="img" aria-label="Tidal Brookfield corner desk return right product photo"></div><span class="badge">NEW COLOUR</span><h2>Tidal Brookfield 1800/900 Corner Desk Return - Right</h2><div class="thumbs" role="img" aria-label="Four configuration views"><span></span><span></span><span></span><span></span></div></article>
      <article class="card"><div class="photo" role="img" aria-label="Tidal Brookfield bow front desk product photo"></div><span class="badge">NEW COLOUR</span><h2>Tidal Brookfield 1800 Bow Front Desk - Full Modesty</h2><div class="thumbs" role="img" aria-label="Four configuration views"><span></span><span></span><span></span><span></span></div></article>
      <article class="card"><div class="photo" role="img" aria-label="Tidal Brookfield desk return product photo"></div><span class="badge">NEW COLOUR</span><h2>Tidal Brookfield Desk Return 1000 x 600</h2><div class="thumbs" role="img" aria-label="Four configuration views"><span></span><span></span><span></span><span></span></div></article>
      <article class="card"><div class="photo" role="img" aria-label="Tidal Brookfield 2400 corner desk product photo"></div><span class="badge">NEW COLOUR</span><h2>Tidal Brookfield 2400 Corner Desk (Right Return)</h2><div class="thumbs" role="img" aria-label="Four configuration views"><span></span><span></span><span></span><span></span></div></article>
    </div>
  </section>
</main>

<footer class="footer">
  <div class="flogo">TIDAL BROOKFIELD</div>
  <div class="follow">FOLLOW</div>
  <div class="socials"><span></span><span></span><span></span><span></span></div>
  <div class="fcol" style="left:268px"><h4>MENU</h4>Desking<br>Seating<br>Storage<br>Screens<br>Tables<br>Reception Counters<br>Accessories<br>Contact Us</div>
  <div class="fcol" style="left:362px"><h4>MY ACCOUNT</h4>My Account<br>Register<br>FAQ<br>Blog<br>Contact</div>
  <div class="fcol" style="left:455px"><h4>LINKS</h4>Home<br>About Us<br>Services<br>Testimonials</div>
  <div class="fcol" style="left:538px"><h4>NEWSLETTER!</h4></div>
  <div class="news"><svg width="8" height="6"><path d="M.5.5h7v5h-7zM.5.5l3.5 3 3.5-3" stroke="#aaa" fill="none"/></svg>E mail id</div>
  <div class="signup">SIGNUP!</div>
</footer>
<div class="base">Copyrights @ 2016 All Rights Reserved</div>
</body>
</html>
```